Upsell Vertical Banner Ad Design For B2B Marketing Agency Vertical 768px × 1180px IS THE SIZE

I need a banner made for my website www.brightlanepromotionhub.biz This banner will be an upsell advertisement for after someone signs up for my monthly program. When they login to their account for the 1st time I will give them the chance to upgrade their account to our annual program with just one click.

this is a page that upsells it currently to give you an idea how we market ourselves:
https://tlpx.pagevault-example.com/page/tlp-annual-upsell

Use this content:

Are You Ready To Commit To Taking Your Business To The Next Level?

Because We're In This For The Long-Haul and Dedicated To Your Success...

Save $300 By Upgrading To An Annual Membership And Pay Only $74/mth

((BUTTON))Yes, Upgrade My Plan Right Now!

*Must prepay the full year at only $898/yr!

Target Market(s)

business owners

Industry/Entity Type

Marketing

Requirements
Must have
• 768px × 1180px IS THE SIZE vertical

Use this content:

Nice to have
• Use this content:

Should not have
• Use this content:

```html
<!DOCTYPE html>
<html lang="en">
<head>
<meta charset="utf-8">
<title>Annual Membership Upsell Banner</title>
<link rel="stylesheet" href="https://fonts.googleapis.com/css2?family=Lato:ital,wght@0,400;0,700;0,900;1,700&display=swap">
<style>
  :root {
    --page-bg: #e4e5e7;
    --white: #ffffff;
    --brand-blue: #1b6fc0;
    --panel-blue: #1f80d2;
    --panel-blue-deep: #1466b2;
    --photo-dark: #17508f;
    --photo-light: #4d9ee0;
    --text-gray: #4b4d50;
    --navy: #16212b;
    --button-red: #c4461d;
  }
  * { box-sizing: border-box; margin: 0; padding: 0; }
  html, body { width: 1200px; height: 1200px; overflow: hidden; }
  body {
    background: var(--page-bg);
    font-family: "Lato", Arial, sans-serif;
    position: relative;
  }
  .banner {
    position: absolute;
    left: 240px; top: 47px;
    width: 720px; height: 1106px;
    background: var(--white);
    overflow: hidden;
  }
  .brand-bar {
    position: absolute; left: 0; top: 0; width: 100%; height: 88px;
    display: flex; align-items: center; justify-content: center; gap: 14px;
  }
  .brand-mark { width: 30px; height: 30px; background: var(--brand-blue); }
  .brand-name {
    color: var(--brand-blue); font-weight: 900; font-size: 28px; letter-spacing: 0.5px;
  }
  .hero-photo {
    position: absolute; left: 0; top: 88px; width: 100%; height: 398px;
    background:
      radial-gradient(circle at 62% 32%, rgba(190,230,255,0.55), rgba(190,230,255,0) 32%),
      linear-gradient(160deg, var(--photo-dark) 0%, var(--photo-light) 55%, var(--panel-blue) 100%);
  }
  .headline-lead {
    position: absolute; left: 44px; top: 290px;
    color: var(--white); font-size: 52px; font-weight: 400; letter-spacing: 1px; line-height: 1;
  }
  .headline-main {
    position: absolute; left: 38px; top: 318px;
    color: var(--white); font-size: 186px; font-weight: 900; line-height: 1; letter-spacing: -2px;
  }
  .headline-tail {
    position: absolute; left: 0; top: 498px; width: 100%;
    text-align: center; color: var(--text-gray);
    font-size: 33px; line-height: 39px; font-weight: 400;
  }
  .headline-tail strong { color: var(--brand-blue); font-weight: 900; }
  .chevron { position: absolute; left: 0; top: 588px; width: 720px; height: 390px; }
  .offer {
    position: absolute; left: 0; top: 730px; width: 100%;
    text-align: center; color: var(--white);
  }
  .offer-intro { font-size: 29px; line-height: 35px; font-weight: 400; }
  .offer-title { font-size: 62px; font-weight: 900; line-height: 1; margin-top: 6px; }
  .offer-rule { width: 528px; height: 3px; background: var(--white); margin: 12px auto 12px; }
  .offer-detail { font-size: 22px; line-height: 29px; font-weight: 400; }
  .offer-detail strong { font-weight: 900; }
  .action-bar {
    position: absolute; left: 0; top: 973px; width: 100%; height: 133px;
    background: var(--navy);
  }
  .action-notch { position: absolute; left: 348px; top: -1px; }
  .upgrade-button {
    position: absolute; left: 85px; top: 31px; width: 547px; height: 54px;
    background: var(--button-red); border: 2px solid var(--white); border-radius: 6px;
    display: flex; align-items: center; justify-content: center; gap: 14px;
    color: var(--white); font-weight: 900; font-size: 25px; text-transform: uppercase;
  }
  .cursor-icon { position: absolute; left: 645px; top: 56px; }
  .fine-print {
    position: absolute; left: 0; top: 100px; width: 100%; text-align: center;
    color: var(--white); font-style: italic; font-weight: 700; font-size: 16px;
  }
</style>
</head>
<body>
  <main class="banner">
    <header class="brand-bar">
      <span class="brand-mark"></span>
      <span class="brand-name">BRIGHT LANE PROMOTION HUB</span>
    </header>

    <div class="hero-photo" role="img" aria-label="Businessman in a suit touching a glowing clock face ringed with dollar signs"></div>

    <h1>
      <span class="headline-lead">ARE YOU</span>
      <span class="headline-main">READY</span>
      <span class="headline-tail">TO COMMIT TO TAKING YOUR<br>BUSINESSES TO <strong>THE NEXT LEVEL</strong>?</span>
    </h1>

    <svg class="chevron" viewBox="0 0 720 390" aria-hidden="true">
      <polygon points="0,78 360,0 720,78 720,390 0,390" fill="var(--panel-blue)"/>
      <polygon points="0,100 360,24 720,100 720,122 360,48 0,122" fill="var(--panel-blue-deep)" opacity="0.7"/>
    </svg>

    <section class="offer">
      <p class="offer-intro">BECAUSE WE’RE IN THIS<br>FOR THE LONG-HAUL &amp; DEDICTED TO</p>
      <p class="offer-title">YOUR SUCCESS!</p>
      <div class="offer-rule"></div>
      <p class="offer-detail"><strong>Save $300</strong> By Upgrading To An Annual Membership<br>And Pay Only $74/mth</p>
    </section>

    <footer class="action-bar">
      <svg class="action-notch" width="24" height="14" viewBox="0 0 24 14" aria-hidden="true">
        <polygon points="0,0 24,0 12,14" fill="var(--panel-blue)"/>
      </svg>
      <div class="upgrade-button">
        <svg width="30" height="30" viewBox="0 0 30 30" aria-hidden="true">
          <rect x="2" y="6" width="20" height="20" fill="var(--white)"/>
          <path d="M6 15 L11 21 L27 3" stroke="var(--button-red)" stroke-width="5" fill="none"/>
          <path d="M6 15 L11 21 L27 3" stroke="var(--white)" stroke-width="2.5" fill="none"/>
        </svg>
        <span>Yes, Upgrade My Plan Right Now!</span>
      </div>
      <svg class="cursor-icon" width="50" height="50" viewBox="0 0 50 50" aria-hidden="true">
        <path d="M20 18 L20 44 L27 37 L32 47 L36 45 L31 35 L41 35 Z" fill="var(--white)"/>
        <g stroke="var(--white)" stroke-width="3" stroke-linecap="round">
          <line x1="16" y1="4" x2="16" y2="11"/>
          <line x1="4" y1="16" x2="11" y2="16"/>
          <line x1="7" y1="7" x2="11" y2="11"/>
          <line x1="25" y1="7" x2="21" y2="11"/>
        </g>
      </svg>
      <p class="fine-print">*Must prepay the full year at only $898/yr!</p>
    </footer>
  </main>
</body>
</html>
```